New VPN Company needs a Web Site

This competition is the first step of a 3 step project.
- Step 1: (This project) We are looking to have 3 pages designed to evaluate your design and illustration skills.
- Step 2: Once we find a winner, we will request a bid to have the rest of the website designed.
- Step 3: We will request a bid to have the designs converted into WordPress if the bid is acceptable.
If you have the capabilities, Steps 2 and 3 can be combined into a single project/bid.
Design Notes
- Design type should be “FLAT.”
- Clean, crisp design that communicates security, anonymity, encryption, privacy.
- Please take a look at the following website: http://brisk.tallowvpn.com This is our current Word Press based setup. It contains all the link structures, menus, and text for the website. PLEASE NOTE THAT THE CURRENT DESIGN HAS NOTHING TO DO WITH WHAT YOU ARE DESIGNING. I USED THE FIRST WORD PRESS TEMPLATE THAT I COULD FIND. Once you submit a winning design, either YOU (if you have the skill set) or somebody else will take the designs and convert it into a word press template.
Here are a few of the pages from http://brisk.tallowvpn.com that I would like to see mockups for:
o Main Page: http://brisk.tallowvpn.com
Notes
• I have a dummy graphic up. That graphic needs to be replaced. Also as per the “Should have’s” I want all pages to have unlimited stretching right and left without that grey border on the right and left sides that are currently present.)
o Features Page: http://brisk.tallowvpn.com/index.php/features/
o Desktop App download Page: http://brisk.tallowvpn.com/index.php/vpn-apps/vpn-for-windows/

- I want a “top bar” which shows Your IP: Your ISP: Your Location: Your Status: Like most of my competitors have.
- This website needs several original illustrations.
- The website must be clean, uncluttered, and concise.
- Use the copy provided from the http://brisk.tallowvpn.com website.
- Colors are up to the designers; this includes logo colors

- Please take a look at some of our competitor's websites for overall inspiration:
o https://www.quarrylantern.com
o https://plumvpn.com
o https://www.fernwickbay.com/en-us/index
o https://www.tidalvpn.com/
o https://www.oakvpn.com/
o https://www.netmoraly.com/
o https://www.lumbrafoxvpn.com/en_US/

Target Market(s)

Consumers between 18-30 from around the world.

Industry/Entity Type

Internet Service Provider

Number of Pages Required

3 page

Colors

Designer to choose colors to be used in the design.

Requirements
Must have
• - Look great on Desktop, Tablet, and smartphones.
• - The current template has borders. I want the new design to stretch with the browser, e.g., no grey borders on the left and right of the screen.
• - All illustration work must be original. We are not interested in stock photos.
• - Use attached logo. Font is Nexa Xbold.
Should not have
• - A nonfunctional look on smartphones. A high percentage of purchases will be made by smartphone users.
• - Should only have solid colors (two tone or three tone is ok). I am not a big fan of gradients or soft shadows.

```html
<!DOCTYPE html>
<html lang="en">
<head>
<meta charset="utf-8">
<title>TallowVPN – Fast and Secure VPN</title>
<link href="https://fonts.googleapis.com/css2?family=Montserrat:wght@400;500;600;700&family=Open+Sans:wght@400;600&display=swap" rel="stylesheet">
<style>
:root{
  --red:#f25c4b;
  --red-dark:#e04a3a;
  --ink:#1f1f24;
  --dark:#2b2930;
  --grey:#6d6d73;
  --light:#f3f3f3;
  --line:#e3e3e3;
  --white:#ffffff;
}
*{box-sizing:border-box;margin:0;padding:0}
html,body{width:1200px;height:3814px;overflow:hidden}
body{font-family:"Open Sans",Arial,sans-serif;color:var(--ink);background:var(--white);position:relative}
a{text-decoration:none}
.abs{position:absolute}
h1,h2,h3,h4,.btn,.nav a,.brand-name{font-family:"Montserrat",Arial,sans-serif}

/* header */
.site-header{position:absolute;left:0;top:0;width:1200px;height:127px;background:var(--dark)}
.topbar{position:absolute;left:0;top:0;width:1200px;height:50px;border-bottom:1px solid #3a3840;font-size:13px;color:#e6e6e6}
.topbar span{position:absolute;top:16px}
.loc-btn{position:absolute;left:864px;top:0;width:166px;height:50px;background:var(--red);color:#fff;font-size:13px;text-align:center;line-height:50px;font-weight:600}
.login{position:absolute;left:1052px;top:16px;font-weight:600}
.brand{position:absolute;left:70px;top:10px;width:110px;text-align:center}
.brand-mark{width:62px;height:62px;border-radius:50%;background:var(--red);margin:0 auto}
.brand-name{display:block;color:#fff;font-weight:700;font-size:15px;margin-top:8px;letter-spacing:.5px}
.nav a{position:absolute;top:74px;color:#fff;font-size:15px;font-weight:500}
.nav a.active{color:var(--red)}

/* hero */
.hero{position:absolute;left:0;top:127px;width:1200px;height:572px;background:#f1f1f1;overflow:hidden}
.hero-art{position:absolute;left:430px;top:0;width:770px;height:572px;background:radial-gradient(circle at 62% 45%,#f7a79c 0,#f26a59 35%,#f3c9c3 62%,#f1f1f1 80%)}
.hero h1{position:absolute;left:76px;top:170px;font-size:58px;font-weight:700;color:var(--red)}
.hero p{position:absolute;left:76px;top:254px;width:390px;font-size:15px;line-height:24px;color:var(--grey)}
.btn{display:inline-block;text-align:center;font-weight:500;font-size:17px}
.btn-solid{background:var(--red);color:#fff}
.hero .btn{position:absolute;left:76px;top:348px;width:272px;height:59px;line-height:59px}

/* guarantee */
.guarantee{position:absolute;left:0;top:699px;width:1200px;height:203px;background:#fff}
.guarantee h2{position:absolute;left:76px;top:40px;font-size:56px;line-height:62px;font-weight:700;color:var(--ink)}
.btn-outline{position:absolute;left:852px;top:76px;width:270px;height:59px;line-height:57px;border:2px solid var(--red);background:var(--red);color:#fff}

/* features */
.features{position:absolute;left:0;top:902px;width:1200px;height:527px;background:var(--light)}
.section-title{position:absolute;left:0;width:1200px;text-align:center;font-size:38px;font-weight:600}
.features .section-title{top:50px}
.feature{position:absolute;top:153px;width:340px;text-align:center}
.feature-icon{width:150px;height:150px;border-radius:50%;background:var(--red);margin:0 auto;display:flex;align-items:center;justify-content:center}
.feature h3{margin-top:48px;font-size:21px;line-height:28px;font-weight:500;text-transform:uppercase}
.features .caption{position:absolute;top:440px;left:0;width:1200px;text-align:center;font-size:12px}

/* benefits */
.benefits{position:absolute;left:0;top:1429px;width:1200px;height:676px;background:var(--red);color:#fff}
.benefits .section-title{top:60px;color:#fff}
.hub{position:absolute;left:505px;top:268px;width:190px;height:190px;border-radius:50%;background:#fff;border:12px solid #f7b8ae}
.hub-core{position:absolute;left:35px;top:35px;width:96px;height:96px;border-radius:50%;background:var(--red)}
.benefit-icon{position:absolute;width:70px;height:70px;border-radius:50%;background:#fff;display:flex;align-items:center;justify-content:center}
.benefit{position:absolute;width:280px}
.benefit h4{font-size:17px;font-weight:600;line-height:22px}
.benefit p{font-size:12px;line-height:18px;color:#fbd3cd;margin-top:6px}
.benefit.left{text-align:right}

/* pricing */
.pricing{position:absolute;left:0;top:2105px;width:1200px;height:551px;background:#fff}
.pricing .section-title{top:58px}
.plan{position:absolute;top:145px;width:330px;height:343px;border:1px solid var(--line);background:#fff;text-align:center;overflow:hidden}
.plan .price{margin-top:42px;font-family:"Montserrat",Arial,sans-serif;color:var(--red);font-size:48px;font-weight:500}
.plan .price sup{font-size:22px;vertical-align:18px}
.plan .price small{font-size:18px}
.plan .save{font-size:13px;color:var(--grey);font-style:italic;margin-top:2px}
.plan .term{display:block;width:190px;height:36px;line-height:36px;margin:24px auto 0;border-radius:18px;background:var(--red);color:#fff;font-family:"Montserrat",Arial,sans-serif;font-weight:600;font-size:16px}
.plan .note{font-size:13px;color:var(--grey);margin-top:34px}
.plan .buy{display:block;width:196px;height:56px;line-height:56px;margin:34px auto 0;background:var(--red);color:#fff;font-family:"Montserrat",Arial,sans-serif;font-size:20px}
.plan.featured{background:var(--red);border-color:var(--red)}
.plan.featured .price,.plan.featured .save,.plan.featured .note{color:#fff}
.plan.featured .term{background:#fff;color:var(--red)}
.plan.featured .buy{background:var(--red);border:3px solid #fff;width:256px;line-height:50px}
.ribbon{position:absolute;left:-34px;top:22px;width:140px;height:22px;background:var(--dark);color:#fff;font-size:9px;font-weight:600;line-height:22px;transform:rotate(-45deg);font-family:"Montserrat",Arial,sans-serif}

/* other benefits */
.other{position:absolute;left:0;top:2656px;width:1200px;height:466px;background:#f4f4f4;overflow:hidden}
.other-art{position:absolute;left:508px;top:0;width:692px;height:466px;background:linear-gradient(100deg,#f4f4f4 0,#dfe3e8 35%,#c9ced6 70%,#b9bfc9 100%)}
.other h2{position:absolute;left:76px;top:70px;font-size:38px;font-weight:600}
.checklist{position:absolute;left:76px;top:146px;list-style:none}
.checklist li{display:flex;align-items:center;height:41px;font-size:14px;color:#44444a}
.checklist svg{margin-right:18px}
.other .btn{position:absolute;left:76px;top:331px;width:222px;height:58px;line-height:58px}

/* streaming */
.streaming{position:absolute;left:0;top:3122px;width:1200px;height:335px;background:#fff}
.tablet-art{position:absolute;left:76px;top:68px;width:471px;height:267px;background:linear-gradient(180deg,#2c2c30,#454549);border-radius:28px 28px 0 0}
.streaming h3{position:absolute;left:628px;top:70px;font-size:20px;font-weight:500}
.streaming p{position:absolute;left:628px;top:112px;width:515px;font-size:14px;line-height:23px;color:#55555b}

/* footer */
.site-footer{position:absolute;left:0;top:3457px;width:1200px;height:357px;background:linear-gradient(180deg,#f06453,#e8503f);color:#fff}
.footer-col{position:absolute;top:62px}
.footer-col h4{font-size:20px;font-weight:600;margin-bottom:22px}
.footer-col p,.footer-col li{font-size:13px;line-height:22px;color:#ffe3df}
.footer-col ul{list-style:none}
.footer-col li{line-height:28px}
.subscribe{position:absolute;left:0;top:84px;display:flex}
.subscribe .field{width:317px;height:51px;background:#fff;color:#aaa;font-size:13px;line-height:51px;padding-left:22px}
.subscribe .submit{width:107px;height:51px;border:2px solid #fff;background:var(--red);color:#fff;font-family:"Montserrat",Arial,sans-serif;font-size:15px;line-height:47px;text-align:center}
.footer-rule{position:absolute;left:76px;top:294px;width:1048px;height:1px;background:#f59a8f}
.copyright{position:absolute;left:0;top:316px;width:1200px;text-align:center;font-size:13px;color:#ffe3df}
</style>
</head>
<body>

<header class="site-header">
  <div class="topbar">
    <span style="left:285px">Your IP Address : 219.91.237.100</span>
    <span style="left:521px">Your ISP : Lorem ipsum</span>
    <span style="left:704px">Status : Unprotected</span>
    <div class="loc-btn">LOCATION ▾</div>
    <span class="login">LOGIN</span>
  </div>
  <div class="brand"><div class="brand-mark"></div><span class="brand-name">TallowVPN</span></div>
  <nav class="nav">
    <a class="active" style="left:578px" href="#">Home</a>
    <a style="left:668px" href="#">Features</a>
    <a style="left:785px" href="#">Van Apps</a>
    <a style="left:910px" href="#">Pricing</a>
    <a style="left:1000px" href="#">Support Center</a>
  </nav>
</header>

<section class="hero">
  <div class="hero-art" role="img" aria-label="Red illustrated globe with glowing network connections"></div>
  <h1>TallowVPN</h1>
  <p>is a fast and ultra secure offshore based VPN solution with thousands of servers in over 40 countries around the globe</p>
  <a class="btn btn-solid" href="#">GET STARTED NOW</a>
</section>

<section class="guarantee">
  <h2>31 Day Unconditional<br>Money Back Guarantee</h2>
  <a class="btn btn-outline" href="#">GET STARTED NOW</a>
</section>

<section class="features">
  <h2 class="section-title">Our VPN FEATURES</h2>
  <div class="feature" style="left:71px">
    <div class="feature-icon"><svg width="70" height="70" viewBox="0 0 70 70" fill="none" stroke="#fff" stroke-width="3"><circle cx="35" cy="35" r="26"/><ellipse cx="35" cy="35" rx="11" ry="26"/><line x1="9" y1="35" x2="61" y2="35"/><line x1="35" y1="9" x2="35" y2="61"/></svg></div>
    <h3>Surf the web<br>anonymously</h3>
  </div>
  <div class="feature" style="left:430px">
    <div class="feature-icon"><svg width="74" height="74" viewBox="0 0 74 74" fill="none" stroke="#fff" stroke-width="3"><path d="M18 42a12 12 0 0 1 3-23 16 16 0 0 1 31 2 10 10 0 0 1 3 21z"/><rect x="28" y="34" width="18" height="32" rx="3"/><path d="M33 34v-5a4 4 0 0 1 8 0v5"/><circle cx="37" cy="50" r="3" fill="#fff"/></svg></div>
    <h3>Make any connection a<br>secure connection</h3>
  </div>
  <div class="feature" style="left:786px">
    <div class="feature-icon"><svg width="76" height="76" viewBox="0 0 76 76" fill="none" stroke="#fff" stroke-width="3"><rect x="10" y="14" width="56" height="40" rx="3"/><line x1="10" y1="22" x2="66" y2="22"/><rect x="26" y="30" width="24" height="14" rx="7"/><line x1="30" y1="62" x2="46" y2="62"/><line x1="38" y1="54" x2="38" y2="62"/></svg></div>
    <h3>Break free from<br>censorship</h3>
  </div>
  <p class="caption">Benefits of using TallowVPN Apps</p>
</section>

<section class="benefits">
  <h2 class="section-title">Benefits of using TallowVPN Apps</h2>
  <svg class="abs" style="left:0;top:0" width="1200" height="676" fill="none" stroke="#fbc5bd" stroke-width="1.5">
    <path d="M430 190 Q540 200 560 262"/>
    <path d="M430 363 L500 363"/>
    <path d="M430 560 Q540 550 560 462"/>
    <path d="M770 200 Q660 200 640 262"/>
    <path d="M770 363 L700 363"/>
    <path d="M770 560 Q660 550 640 462"/>
  </svg>
  <div class="hub"><div class="hub-core"></div></div>

  <div class="benefit left" style="left:80px;top:163px"><h4>Military grade 256 bit<br>encryption</h4><p>Nobody can spy on your internet activities because we route it through securely encrypted tunnels</p></div>
  <div class="benefit-icon" style="left:365px;top:155px"><svg width="34" height="34" viewBox="0 0 34 34" fill="none" stroke="#8a8a90" stroke-width="2.5"><path d="M17 3l12 5v9c0 7-5 12-12 14C10 29 5 24 5 17V8z"/></svg></div>

  <div class="benefit left" style="left:80px;top:330px"><h4>Absolute NO<br>LOGGING Policy</h4><p>We do not permanently log any of your online activities.</p></div>
  <div class="benefit-icon" style="left:365px;top:328px"><svg width="34" height="34" viewBox="0 0 34 34" fill="none" stroke="#8a8a90" stroke-width="2.5"><path d="M6 28L28 6v22z"/></svg></div>

  <div class="benefit left" style="left:80px;top:520px"><h4>Unlimited Bandwidth</h4><p>TallowVPN works flawlessly with your favorite streaming channels such as Streamly, Reelbox etc.</p></div>
  <div class="benefit-icon" style="left:365px;top:525px"><svg width="40" height="24" viewBox="0 0 40 24" fill="none" stroke="#8a8a90" stroke-width="3"><path d="M20 12c-4-6-8-8-12-8a8 8 0 0 0 0 16c4 0 8-2 12-8s8-8 12-8a8 8 0 0 1 0 16c-4 0-8-2-12-8z"/></svg></div>

  <div class="benefit-icon" style="left:765px;top:155px"><svg width="34" height="30" viewBox="0 0 34 30" fill="none" stroke="#8a8a90" stroke-width="2.5"><path d="M3 11a20 20 0 0 1 28 0M8 16a13 13 0 0 1 18 0M13 21a6 6 0 0 1 8 0"/><circle cx="17" cy="26" r="2" fill="#8a8a90"/></svg></div>
  <div class="benefit" style="left:855px;top:163px"><h4>Secure your public Wi-Fi<br>connections</h4><p>Use any public Wi-Fi network knowing that nobody can intercept your traffic or spy on you.</p></div>

  <div class="benefit-icon" style="left:765px;top:328px"><svg width="34" height="34" viewBox="0 0 34 34" fill="none" stroke="#8a8a90" stroke-width="2.5"><rect x="4" y="5" width="16" height="24" rx="2"/><rect x="20" y="12" width="10" height="17" rx="2"/></svg></div>
  <div class="benefit" style="left:855px;top:345px"><h4>Multiple Devices</h4><p>Use TallowVPN on 10 devices simultaneously</p></div>

  <div class="benefit-icon" style="left:765px;top:525px"><svg width="36" height="32" viewBox="0 0 36 32" fill="none" stroke="#333" stroke-width="2.5"><rect x="3" y="3" width="24" height="17" rx="2"/><line x1="10" y1="26" x2="20" y2="26"/><rect x="22" y="14" width="11" height="15" rx="2"/></svg></div>
  <div class="benefit" style="left:855px;top:530px"><h4>P2P Friendly</h4><p>We allow P2P traffic on our highly optimized servers.</p></div>
</section>

<section class="pricing">
  <h2 class="section-title">Our PRICING</h2>
  <div class="plan" style="left:79px">
    <div class="price"><sup>$</sup>10.95<small> / monthly</small></div>
    <div class="save">(No saving)</div>
    <span class="term">MONTHLY</span>
    <p class="note">31 Day Money Back Guarantee</p>
    <a class="buy" href="#">Get TallowVPN</a>
  </div>
  <div class="plan featured" style="left:435px">
    <div class="ribbon">MOST POPULAR</div>
    <div class="price"><sup>$</sup>3.51<small> / monthly</small></div>
    <div class="save">(SAVE 68%)</div>
    <span class="term">TWO YEAR</span>
    <p class="note">31 Day Money Back Guarantee</p>
    <a class="buy" href="#">Get TallowVPN NOW</a>
  </div>
  <div class="plan" style="left:791px">
    <div class="price"><sup>$</sup>5.41<small> / monthly</small></div>
    <div class="save">(SAVE 51%)</div>
    <span class="term">YEARLY</span>
    <p class="note">31 Day Money Back Guarantee</p>
    <a class="buy" href="#">Get TallowVPN</a>
  </div>
</section>

<section class="other">
  <div class="other-art" role="img" aria-label="Photo of hands holding a smartphone"></div>
  <h2>Our other BENEFITS</h2>
  <ul class="checklist">
    <li><svg width="26" height="22" viewBox="0 0 26 22" fill="none" stroke="var(--red)" stroke-width="2"><rect x="1" y="4" width="16" height="16"/><path d="M5 11l5 5L24 2"/></svg>Apps for all of your favorite devices</li>
    <li><svg width="26" height="22" viewBox="0 0 26 22" fill="none" stroke="var(--red)" stroke-width="2"><rect x="1" y="4" width="16" height="16"/><path d="M5 11l5 5L24 2"/></svg>X000 IP addresses from across the globe</li>
    <li><svg width="26" height="22" viewBox="0 0 26 22" fill="none" stroke="var(--red)" stroke-width="2"><rect x="1" y="4" width="16" height="16"/><path d="M5 11l5 5L24 2"/></svg>256 bit AES encryption</li>
    <li><svg width="26" height="22" viewBox="0 0 26 22" fill="none" stroke="var(--red)" stroke-width="2"><rect x="1" y="4" width="16" height="16"/><path d="M5 11l5 5L24 2"/></svg>OpenVPN/IKEv2/L2TP/IPsec/PPTP/SSTP protocol support</li>
  </ul>
  <a class="btn btn-solid" href="#">LEARN MORE</a>
</section>

<section class="streaming">
  <div class="tablet-art" role="img" aria-label="Hands holding a tablet showing the app start screen"></div>
  <h3>Watch Your Favorite Streaming Channels</h3>
  <p>TallowVPN works flawlessly with your favorite streaming channels such as Streamly, Reelbox etc. Your ISP might monitor your activity and throttle your internet speed. When using TallowVPN your ISP only sees encrypted data and is unable to throttle your internet speed based on your activity. TallowVPN allows you to bypass location-based blocks and access global streaming services no matter your physical location.</p>
</section>

<footer class="site-footer" role="img" aria-label="Red tinted city skyline at dusk">
  <div class="footer-col" style="left:76px;width:300px">
    <h4>ABOUT US</h4>
    <p>is a fast and ultra secure offshore based VPN solution with thousands of servers in over 40 countries around the globe.</p>
  </div>
  <div class="footer-col" style="left:457px">
    <h4>USEFUL LINKS</h4>
    <ul>
      <li>VPN FOR DESKTOP</li>
      <li>VPN FOR LAPTOP</li>
      <li>VPN FOR PHONE &amp; TABLET</li>
      <li>VPN FOR MOBILE</li>
      <li>VPN FOR BROWSER</li>
    </ul>
  </div>
  <div class="footer-col" style="left:674px;width:430px">
    <h4>NEWSLETTER</h4>
    <p>Sign up for our regular informational newsletters</p>
    <div class="subscribe"><div class="field">Enter Your E-Mail Id</div><div class="submit">SUBMIT</div></div>
  </div>
  <div class="footer-rule"></div>
  <p class="copyright">© TallowVPN – 2018. All Rights Reserved</p>
</footer>

</body>
</html>
```